Business card update

Opening a subsidiary of my company in the USA and need to update my logo.
Updates

I made a mistake on my briefing. It's only the business card. Thanks for alerting me on the mistake.

All the best

Gustavo

Target Market(s)

We are an Executive Search company and our target audience are executives in large corporations.

Industry/Entity Type

Business

Requirements
Must have
• Keep the logo. In the US the company is called Dario Kellner Executive Search.

```html
<!DOCTYPE html>
<html lang="en">
<head>
<meta charset="utf-8">
<title>Dario Kellner Executive Search – Business Card</title>
<link rel="stylesheet" href="https://fonts.googleapis.com/css2?family=Bitter:wght@400;700;800&display=swap">
<style>
  :root {
    --page-bg: #f4f6f6;
    --card-top: #bfe3e2;
    --card-mid: #7fd0cd;
    --card-bottom: #27b9b4;
    --teal: #2bbdb7;
    --teal-deep: #14a59c;
    --ink: #1d1d1d;
    --white: #ffffff;
  }
  * { box-sizing: border-box; margin: 0; padding: 0; }
  html, body {
    width: 1200px; height: 1000px; overflow: hidden;
    background: var(--page-bg);
    font-family: "Bitter", Georgia, serif;
  }
  .canvas {
    position: relative; width: 1200px; height: 1000px;
  }
  .card {
    position: absolute; left: 100px; top: 210px;
    width: 1000px; height: 580px;
    border-radius: 14px; overflow: hidden;
    background: linear-gradient(180deg, var(--card-top) 0%, var(--card-mid) 55%, var(--card-bottom) 100%);
    box-shadow: 0 18px 40px rgba(0,0,0,.12);
  }
  .pattern {
    position: absolute;
  }
  .pattern--left {
    left: 0; top: 0; width: 310px; height: 580px;
    background: linear-gradient(160deg, rgba(43,189,183,.35) 0%, rgba(20,165,156,.55) 100%);
    -webkit-mask-image: linear-gradient(90deg, #000 55%, transparent 100%);
            mask-image: linear-gradient(90deg, #000 55%, transparent 100%);
  }
  .pattern--right {
    right: 0; bottom: 0; width: 330px; height: 460px;
    background: linear-gradient(200deg, rgba(43,189,183,.3) 0%, rgba(20,165,156,.6) 100%);
    -webkit-mask-image: linear-gradient(270deg, #000 55%, transparent 100%);
            mask-image: linear-gradient(270deg, #000 55%, transparent 100%);
  }
  .brand {
    position: absolute; left: 250px; top: 40px; width: 500px;
    text-align: center;
  }
  .brand__rule {
    height: 3px; background: var(--teal); margin: 0 30px;
  }
  .brand__name {
    display: flex; align-items: center; justify-content: center; gap: 16px;
    padding: 14px 0;
    font-size: 40px; font-weight: 400; letter-spacing: 10px; color: var(--ink);
  }
  .brand__mark {
    width: 26px; height: 26px; border-radius: 50%; background: var(--teal);
  }
  .details {
    position: absolute; left: 290px; top: 150px; width: 420px;
    text-align: center; color: var(--ink);
  }
  .company__line1 { font-size: 27px; font-weight: 400; line-height: 1.1; }
  .company__line2 { font-size: 32px; font-weight: 800; line-height: 1.15; }
  .details__rule {
    height: 3px; background: var(--teal); margin: 10px 0 12px;
  }
  .person { font-size: 24px; margin-bottom: 8px; }
  .label {
    font-size: 15px; font-weight: 700; color: var(--white); line-height: 1.2;
  }
  .value { font-size: 21px; line-height: 1.25; margin-bottom: 4px; }
  .website {
    margin-top: 14px; font-size: 25px; font-weight: 700; color: var(--white);
  }
</style>
</head>
<body>
<main class="canvas">
  <section class="card">
    <div class="pattern pattern--left" role="img" aria-label="Decorative field of teal dot columns and chevron arrows"></div>
    <div class="pattern pattern--right" role="img" aria-label="Decorative field of teal dot columns and chevron arrows"></div>

    <header class="brand">
      <div class="brand__rule"></div>
      <div class="brand__name"><span>DARIO</span><span class="brand__mark"></span><span>KELLNER</span></div>
      <div class="brand__rule"></div>
    </header>

    <div class="details">
      <div class="company__line1">Dario Kellner</div>
      <div class="company__line2">Executive Search</div>
      <div class="details__rule"></div>
      <div class="person">Gustavo R. Kellner</div>
      <div class="label">Phone:</div>
      <div class="value">305 555-0148</div>
      <div class="label">E-mail:</div>
      <div class="value">gkellner@dkexecutivesearch.com</div>
      <div class="label">Address:</div>
      <div class="value">4410 Harbor View Ave Suite 300<br>Coral Bay FL 33140</div>
      <div class="website">www.dkexecutivesearch.com</div>
    </div>
  </section>
</main>
</body>
</html>
```